Torvel Cleaning Company Flyer

Hi, We need an A4 flyer design for our cleaning company, focusing on dry carpet cleaning I attached our catalogue to give some idea. In addition, our websites can provide more information. Our Services:-General Cleaning Carry out heavy cleansing tasks and special projects. Clean, stock and supply designated facility areas (dusting, sweeping, vacuuming, mopping, cleaning ceiling vents, restroom cleaning etc).Using electrically powered scrubbing and polishing machines to burnish, scrub, polish and spray clean floors. Window Cleaning Regular, Reliable Window Cleaning.Hard To Reach Windows.Single 7 Multi-Storey.Frames and Glass Cleaned.Floor Cleaning Cleaning Marble Cleaning & Polishing.Tile & Grout Cleaning.Hardwood Floors Services.Vinyl Floors.The MIRA Dry Extraction Carpet Cleaning System uses environmentally preferred, Blue Fern Certified cleaning products that deep cleans your carpets and textured hard floors quickly and easily.

Target Market(s)

Commercial Cleaning residential Cleaning Hotel cleaning

Industry/Entity Type

Cleaning Service

Contact Information for Business Card

Samir Tareq Al-Hudhaili Gm
Derek Plume Marketing Manger

Font styles to use
Serif
Sans Serif

Colors
0355a3
3176b5
85acd3
cee9f5
85cae6
34a6d7
0592cd

```html
<!DOCTYPE html>
<html lang="en">
<head>
<meta charset="utf-8">
<title>Torvel Cleaning Flyer</title>
<link href="https://fonts.googleapis.com/css2?family=Quicksand:wght@500;700&family=Roboto:wght@400;700&family=Cairo:wght@600&display=swap" rel="stylesheet">
<style>
  :root {
    --navy: #0355a3;
    --ink: #1b2f6e;
    --mid-blue: #3176b5;
    --soft-blue: #85acd3;
    --ice: #cee9f5;
    --sky: #85cae6;
    --bright: #34a6d7;
    --cyan: #0592cd;
    --white: #ffffff;
  }
  html, body { margin: 0; padding: 0; overflow: hidden; }
  body { width: 849px; height: 1200px; background: var(--white); }
  .flyer { position: relative; width: 849px; height: 1200px; overflow: hidden; font-family: "Roboto", Arial, sans-serif; }
  .flyer-bg { position: absolute; inset: 0; }

  .brand { position: absolute; left: 48px; top: 56px; width: 300px; color: var(--ink); }
  .brand-name { font-family: "Quicksand", Arial, sans-serif; font-weight: 700; font-size: 50px; line-height: 1; margin: 0; display: flex; align-items: center; gap: 12px; }
  .brand-name::before { content: ""; width: 22px; height: 22px; border-radius: 50%; background: var(--bright); }
  .brand-sub { font-family: "Quicksand", Arial, sans-serif; font-weight: 700; font-size: 28px; margin: 6px 0 0 34px; }
  .brand-arabic { position: absolute; left: 0; top: 158px; font-family: "Cairo", sans-serif; font-weight: 600; font-size: 20px; color: #111; direction: rtl; width: 270px; text-align: center; margin: 0; }
  .brand-est { position: absolute; left: 0; top: 194px; font-family: "Roboto", Arial, sans-serif; font-weight: 700; font-size: 21px; letter-spacing: 3px; color: #111; margin: 0; white-space: nowrap; }

  .headline { position: absolute; left: 18px; top: 592px; color: var(--white); font-family: "Quicksand", Arial, sans-serif; font-weight: 700; transform: rotate(-5deg); transform-origin: left top; display: flex; align-items: center; gap: 18px; }
  .headline-dry { font-size: 122px; line-height: 1; letter-spacing: -2px; }
  .headline-rest { font-size: 54px; line-height: 1; }

  .service { position: absolute; color: var(--white); }
  .service-title { font-family: "Quicksand", Arial, sans-serif; font-weight: 700; margin: 0; line-height: 1.05; position: relative; }
  .service-list { position: absolute; background: var(--white); border-radius: 12px; color: #111; font-family: "Quicksand", Arial, sans-serif; font-weight: 700; margin: 0; list-style: none; }
  .window .service-title { font-size: 36px; left: 600px; top: 578px; position: absolute; width: 230px; }
  .window .service-list { left: 606px; top: 660px; width: 214px; padding: 8px 0 10px 20px; font-size: 12.5px; line-height: 1.3; box-sizing: border-box; }
  .general .service-title { font-size: 29px; position: absolute; left: 425px; top: 800px; white-space: nowrap; }
  .general .service-list { left: 436px; top: 837px; width: 244px; padding: 16px 12px 12px 24px; font-size: 12px; line-height: 1.3; box-sizing: border-box; }

  .address { position: absolute; left: 418px; top: 972px; transform: rotate(-8deg); transform-origin: left top; color: var(--ink); font-family: "Quicksand", Arial, sans-serif; font-weight: 700; text-align: right; width: 420px; }
  .address-street { font-size: 24px; display: block; }
  .address-country { font-size: 36px; display: block; margin-top: -4px; }

  .equipment { position: absolute; left: 64px; top: 768px; width: 288px; height: 288px; border-radius: 50%; background: var(--white); }
  .equipment-photo { position: absolute; inset: 20px; border-radius: 50%; background: radial-gradient(circle, #c9cfe2 0%, #e9ecf4 70%); }

  .system { position: absolute; left: 110px; top: 1104px; display: flex; gap: 20px; }
  .system-mark { width: 108px; color: var(--ink); font-family: "Roboto", Arial, sans-serif; }
  .system-name { font-weight: 700; font-size: 44px; line-height: 1; margin: 0; }
  .system-caption { font-size: 9.5px; line-height: 1.15; margin: 4px 0 0; border-top: 1px solid var(--ink); padding-top: 3px; }
  .system-copy { font-size: 15.5px; line-height: 18.5px; color: #222; margin: 2px 0 0; width: 420px; }
  .system-copy strong { font-weight: 700; }
</style>
</head>
<body>
<main class="flyer">
  <svg class="flyer-bg" width="849" height="1200" viewBox="0 0 849 1200">
    <defs>
      <linearGradient id="deep" x1="0" y1="0" x2="1" y2="1">
        <stop offset="0" stop-color="#0355a3"/>
        <stop offset="0.5" stop-color="#0592cd"/>
        <stop offset="1" stop-color="#3176b5"/>
      </linearGradient>
      <linearGradient id="pale" x1="0" y1="0" x2="1" y2="1">
        <stop offset="0" stop-color="#cee9f5"/>
        <stop offset="1" stop-color="#ffffff"/>
      </linearGradient>
      <linearGradient id="photo" x1="0" y1="0" x2="0" y2="1">
        <stop offset="0" stop-color="#8a5a3a"/>
        <stop offset="0.55" stop-color="#a47454"/>
        <stop offset="0.75" stop-color="#d8cbbb"/>
        <stop offset="1" stop-color="#e6ddd2"/>
      </linearGradient>
    </defs>
    <rect x="0" y="0" width="849" height="640" fill="url(#photo)" role="img" aria-label="Photo of a technician in a company polo shirt running a floor polishing machine over a marble entrance floor"/>
    <polygon points="0,608 849,488 849,1200 0,1200" fill="url(#deep)"/>
    <polygon points="849,700 849,820 520,940 430,900" fill="#34a6d7" opacity="0.35"/>
    <polygon points="0,900 600,780 849,840 0,1020" fill="#3176b5" opacity="0.35"/>
    <polygon points="0,1072 849,904 849,1200 0,1200" fill="url(#pale)"/>
    <polygon points="0,640 512,524 496,728 0,736" fill="#34a6d7"/>
    <polygon points="0,0 440,0 452,316 0,360" fill="#ffffff"/>
    <polygon points="584,576 760,592 822,612 808,668 580,672" fill="#34a6d7"/>
    <polygon points="420,808 720,796 716,836 424,842" fill="#34a6d7"/>
  </svg>

  <header class="brand">
    <p class="brand-name">Torvel</p>
    <p class="brand-sub">Cleaning</p>
    <p class="brand-arabic">مؤسسة تورفل للتنظيفات</p>
    <p class="brand-est">Torvel Cleaning Est.</p>
  </header>

  <h1 class="headline">
    <span class="headline-dry">DRY</span>
    <span class="headline-rest">CARPET<br>CLEANING</span>
  </h1>

  <section class="service window">
    <h2 class="service-title">WINDOW CLEANING</h2>
    <ul class="service-list">
      <li>Reliable Window Cleaning</li>
      <li>Hard To Reach Windows</li>
      <li>Single &amp; Multi-Storey</li>
      <li>Frames and Glass Cleaned</li>
    </ul>
  </section>

  <section class="service general">
    <h2 class="service-title">GENERAL CLEANING</h2>
    <p class="service-list">Dusting, Sweeping, Vacuuming, Mopping, Cleaning ceiling vents, Restroom cleaning etc.</p>
  </section>

  <div class="equipment">
    <div class="equipment-photo" role="img" aria-label="Dry extraction carpet cleaning machines with buckets and bottles of cleaning compound"></div>
  </div>

  <p class="address">
    <span class="address-street">Al Nakheel Garden Street, Doha</span>
    <span class="address-country">Qatar</span>
  </p>

  <footer class="system">
    <div class="system-mark">
      <p class="system-name">MIRA</p>
      <p class="system-caption">The Dry Extraction Carpet Cleaning System</p>
    </div>
    <p class="system-copy"><strong>The MIRA Dry</strong> Extraction Carpet Cleaning System uses environmentally preferred, Blue Fern Certified cleaning products that deep cleans your carpets and textured hard floors quickly and easily.</p>
  </footer>
</main>
</body>
</html>
```